Beauty website banner

We are an Australian beauty website selling mid and high end cosmetics and beauty products.

We need a banner that tells customers they can share their product wishlists with friends to let them know what they want for Christmas.

Target Market(s)

Female, 30-60, white collar

Industry/Entity Type

Cosmetics

Requirements
Must have
• 600 x 150 pixels in size

Words to be as follows, not including the (") of course.

"Share your wishlist with friends and family for Christmas!"

(Then in smaller font) "Just log in to your account, go to your wishlist and click on the ‘share wishlist’ button"

```html
<!DOCTYPE html>
<html lang="en">
<head>
<meta charset="utf-8">
<title>Share your wishlist for Christmas</title>
<link rel="stylesheet" href="https://fonts.googleapis.com/css2?family=Pinyon+Script&family=Cinzel:wght@400;500&family=Arimo&display=swap">
<style>
  :root {
    --page: #ffffff;
    --frame: #3f7fbf;
    --sky-light: #f7fbfe;
    --sky-mid: #d6e8f4;
    --sky-deep: #9fc9e6;
    --ink: #2a2a2a;
    --ink-soft: #3b3b3b;
    --skin: #f1c9ad;
    --mouse: #e9edf0;
  }
  html, body {
    margin: 0;
    width: 1200px;
    height: 894px;
    overflow: hidden;
    background: var(--page);
  }
  .banner {
    position: absolute;
    left: 6px;
    top: 300px;
    width: 1186px;
    height: 292px;
    border: 3px solid var(--frame);
    background:
      radial-gradient(ellipse 260px 220px at 0% 80%, var(--sky-deep), transparent 70%),
      linear-gradient(90deg, var(--sky-mid) 0%, var(--sky-light) 35%, #ffffff 60%, #ffffff 100%);
    overflow: hidden;
    font-family: "Arimo", Arial, sans-serif;
  }
  .hand-photo {
    position: absolute;
    left: 720px;
    top: 40px;
    width: 470px;
    height: 200px;
    background:
      radial-gradient(ellipse 190px 90px at 70% 45%, var(--skin), rgba(241,201,173,0) 75%),
      radial-gradient(ellipse 150px 40px at 35% 68%, var(--mouse), rgba(233,237,240,0) 80%);
  }
  .headline {
    position: absolute;
    left: 50px;
    top: 30px;
    margin: 0;
    font-weight: normal;
    color: var(--ink);
  }
  .headline-initial {
    position: absolute;
    left: 0;
    top: 0;
    font-family: "Cinzel", Georgia, serif;
    font-size: 92px;
    line-height: 1;
  }
  .headline-script {
    position: absolute;
    left: 52px;
    top: 20px;
    white-space: nowrap;
    font-family: "Pinyon Script", cursive;
    font-size: 42px;
    line-height: 1;
  }
  .headline-occasion {
    position: absolute;
    left: 60px;
    top: 92px;
    white-space: nowrap;
    font-family: "Cinzel", Georgia, serif;
    font-size: 66px;
    line-height: 1;
    letter-spacing: 1px;
  }
  .headline-occasion .cap {
    font-size: 94px;
  }
  .instructions {
    position: absolute;
    left: 58px;
    top: 246px;
    margin: 0;
    white-space: nowrap;
    font-size: 22px;
    color: var(--ink-soft);
  }
</style>
</head>
<body>
  <section class="banner">
    <div class="hand-photo" role="img" aria-label="Photo of a hand resting on a white computer mouse"></div>
    <h1 class="headline">
      <span class="headline-initial">S</span>
      <span class="headline-script">hare your wishlist with friends and family for</span>
      <span class="headline-occasion"><span class="cap">C</span>HRISTMAS!</span>
    </h1>
    <p class="instructions">Just log in to your account, go to your wishlist and click on the ‘share wishlist’ button</p>
  </section>
</body>
</html>
```